Bright Wallet Blueprint: 8 Simple Moves To Put Your Cash Affairs Straight

Need a book cover for a book called "Bright Wallet Blueprint: 8 Moves To Put Your Cash Affairs Straight"

The book is 5.5 by 8.5 and has no spine.

I am attaching the current cover but would like to see some other options that you all can come up with.

This book contains 8 specific action items for what people need to do.
Pay down debt. get estate documents in order. Be careful when buying a house, have enough life insurance to pay debt...etc.

Target Market(s)

Target market is parents around 35-55 years old who are concerned about their financial situation.

Industry/Entity Type

Financial Planning

Font styles to use
Serif

Colors

Designer to choose colors to be used in the design.

Requirements
Must have
• Definitely want my picture on the back.
Nice to have
• I'm pretty much open to ideas.

```html
<!DOCTYPE html>
<html lang="en">
<head>
<meta charset="utf-8">
<title>Bright Wallet Blueprint – Book Cover</title>
<link href="https://fonts.googleapis.com/css2?family=Cinzel:wght@400;600;700&family=Source+Sans+3:wght@400;600;700&family=Arimo:wght@700&display=swap" rel="stylesheet">
<style>
  :root {
    --title-grey: #8e8e8e;
    --white: #ffffff;
    --yellow: #f7d51e;
    --panel-yellow: rgba(246, 208, 40, 0.82);
    --panel-yellow-edge: #e2b913;
    --panel-dark: rgba(20, 18, 16, 0.86);
    --red: #e41e1e;
    --ink: #111111;
  }
  * { margin: 0; padding: 0; box-sizing: border-box; }
  html, body { width: 1200px; height: 887px; overflow: hidden; background: #fff; }
  .cover {
    position: relative;
    width: 1200px;
    height: 887px;
    overflow: hidden;
    font-family: "Source Sans 3", sans-serif;
  }
  .cover-photo {
    position: absolute; inset: 0;
    background:
      radial-gradient(ellipse 320px 420px at 700px 520px, rgba(60,50,45,0.55), transparent 70%),
      radial-gradient(ellipse 300px 460px at 1010px 560px, rgba(40,40,45,0.6), transparent 70%),
      radial-gradient(ellipse 420px 300px at 280px 760px, rgba(70,70,60,0.55), transparent 75%),
      linear-gradient(180deg, #ffffff 0%, #f4f4f1 30%, #b9b7ae 62%, #55524c 100%);
  }
  .back-title, .front-title {
    position: absolute;
    font-family: "Cinzel", serif;
    text-transform: uppercase;
    letter-spacing: 1px;
  }
  .back-title span, .front-title span { display: block; line-height: 0.92; }
  .back-title { left: 38px; top: 40px; color: var(--title-grey); font-weight: 600; }
  .back-title .line-sm { font-size: 64px; }
  .back-title .line-lg { font-size: 92px; }
  .front-title {
    right: 58px; top: 436px; text-align: center;
    color: var(--white); font-weight: 700;
    text-shadow: 0 2px 6px rgba(0,0,0,0.45);
  }
  .front-title .line-sm { font-size: 68px; }
  .front-title .line-lg { font-size: 100px; color: var(--yellow); }
  .author-name {
    position: absolute; right: 69px; top: 146px;
    font-family: "Arimo", sans-serif; font-weight: 700; font-size: 31px; color: var(--ink);
  }
  .bio-panel {
    position: absolute; left: 0; top: 298px; width: 578px; height: 237px;
    background: var(--panel-yellow);
    border: 3px solid var(--panel-yellow-edge); border-left: none;
    border-radius: 0 26px 26px 0;
  }
  .headshot {
    position: absolute; left: 22px; top: 2px; width: 226px; height: 228px;
    border-radius: 22px;
    background: linear-gradient(180deg, #8a8f86 0%, #b6b0a5 45%, #6d6f72 100%);
  }
  .bio-text {
    position: absolute; left: 268px; top: 20px; width: 282px;
    font-size: 19.5px; line-height: 1.23; color: var(--ink); text-align: justify;
  }
  .bio-text strong { font-size: 23px; font-weight: 600; }
  .praise-panel {
    position: absolute; left: 20px; top: 550px; width: 572px; height: 168px;
    background: var(--panel-dark);
    border: 3px solid var(--red); border-radius: 28px;
    padding: 16px 22px 0 20px; color: var(--white);
  }
  .praise-heading { font-size: 22px; font-weight: 400; color: var(--yellow); margin-bottom: 4px; }
  .praise-heading strong { font-weight: 700; }
  .praise-quote { font-size: 15.6px; line-height: 1.28; text-align: justify; }
  .praise-source { font-size: 15px; font-weight: 700; margin-top: 2px; }
  .availability {
    position: absolute; left: 42px; top: 734px; width: 420px;
    color: var(--white); font-size: 17px; line-height: 1.3;
    text-shadow: 0 1px 3px rgba(0,0,0,0.5);
  }
  .availability strong { font-weight: 700; font-size: 18px; }
  .price {
    position: absolute; left: 42px; top: 814px;
    color: var(--white); font-weight: 700; font-size: 18px;
  }
  .subtitle-band {
    position: absolute; left: 646px; top: 704px; width: 580px; height: 138px;
    background: var(--panel-dark);
    border: 5px solid var(--red); border-radius: 70px 0 0 70px;
  }
  .subtitle-number {
    position: absolute; left: 56px; top: 12px;
    font-family: "Arimo", sans-serif; font-weight: 700; font-size: 100px; line-height: 1;
    color: var(--yellow); text-shadow: 3px 3px 4px rgba(0,0,0,0.6);
  }
  .subtitle-text {
    position: absolute; left: 140px; top: 30px; width: 400px;
    font-family: "Arimo", sans-serif; font-weight: 700; font-size: 24px; line-height: 1.38;
    color: var(--white); text-shadow: 2px 2px 3px rgba(0,0,0,0.6);
    white-space: nowrap;
  }
</style>
</head>
<body>
<main class="cover">
  <div class="cover-photo" role="img" aria-label="Photo of a smiling woman and man looking up as banknotes fall around them"></div>

  <h2 class="back-title">
    <span class="line-sm">Bright</span>
    <span class="line-lg">Wallet</span>
    <span class="line-sm">Blueprint</span>
  </h2>

  <section class="bio-panel">
    <div class="headshot" role="img" aria-label="Portrait photo of the author in a grey suit"></div>
    <p class="bio-text"><strong>Drew Halloway</strong> has provided financial advice since 1998 in areas of investment management, Social Security, tax, retirement planning and wealth transfer strategies. Drew believes that complexity is the enemy of successful financial planning.</p>
  </section>

  <section class="praise-panel">
    <h3 class="praise-heading">PRAISE FOR <strong>BRIGHT WALLET BLUEPRINT</strong></h3>
    <p class="praise-quote">“Beginning with prudent advice on debt and debt management and concluding with reasons for estate planning at an early age, Halloway provides simple yet applicable strategies for anyone to use confidently – and secure a more stable financial future. About as real and raw as it comes.”</p>
    <p class="praise-source">- Marla Quintero, Westbrook, Oregon</p>
  </section>

  <p class="availability"><strong>Bright Wallet Blueprint</strong> is available at www.northfieldwealthplan.com, or by emailing Drew@northfieldwealthplan.com.</p>
  <p class="price">$18.95</p>

  <p class="author-name">DREW HALLOWAY, CWA, MS</p>

  <h1 class="front-title">
    <span class="line-sm">Bright</span>
    <span class="line-lg">Wallet</span>
    <span class="line-sm">Blueprint</span>
  </h1>

  <div class="subtitle-band">
    <span class="subtitle-number">8</span>
    <p class="subtitle-text">SIMPLE MOVES TO PUT YOUR<br>CASH AFFAIRS STRAIGHT</p>
  </div>
</main>
</body>
</html>
```